Business Card Design

We require a business card design for a law firm, our signature colours are maroon and cream. Our slogan is "From our family to yours", we would like the cards to be professional however feminine at the same time.

Industry/Entity Type

Business

Contact Information for Business Card

Helena Brackett & Associates Lawyers & Conveyancers, Helena Brackett LL.B. Principal Solicitor, 17 Quillon Street, Marrowdale NSW 2190

Logo styles of interest
Emblem Logo
Abstract Logo
Wordmark Logo

```html
<!DOCTYPE html>
<html lang="en">
<head>
<meta charset="utf-8">
<title>Helena Brackett &amp; Associates – Business Card</title>
<link rel="stylesheet" href="https://fonts.googleapis.com/css2?family=EB+Garamond:ital,wght@0,400;0,500;1,400&display=swap">
<style>
  :root {
    --maroon: #5f0f24;
    --maroon-light: #6e1a30;
    --maroon-edge: #3a0714;
    --cream: #f6f5bc;
    --cream-text: #f7f1cf;
    --serif: "EB Garamond", Garamond, "Times New Roman", serif;
  }
  html, body {
    margin: 0;
    padding: 0;
    width: 1200px;
    height: 741px;
    overflow: hidden;
    background: #ffffff;
  }
  .card {
    position: relative;
    width: 1200px;
    height: 741px;
    overflow: hidden;
    font-family: var(--serif);
    box-sizing: border-box;
    border: 3px solid var(--maroon-edge);
  }
  .card__backdrop {
    position: absolute;
    inset: 0;
    background: radial-gradient(ellipse at 60% 40%, var(--maroon-light) 0%, var(--maroon) 70%);
  }
  .logo-panel {
    position: absolute;
    left: 83px;
    top: 168px;
    width: 422px;
    height: 356px;
    background: var(--cream);
    display: flex;
    flex-direction: column;
    align-items: center;
    justify-content: center;
  }
  .logo-panel__name {
    margin: 0;
    color: var(--maroon);
    font-weight: 400;
    font-size: 30px;
    line-height: 1.25;
    text-align: center;
  }
  .firm-title {
    position: absolute;
    right: 79px;
    top: 72px;
    margin: 0;
    color: var(--cream-text);
    font-weight: 400;
    font-size: 34px;
    line-height: 47px;
    text-align: right;
  }
  .firm-title__line { display: block; }
  .firm-title__line--first { margin-right: 11px; }
  .contact {
    position: absolute;
    right: 79px;
    top: 276px;
    text-align: right;
    color: var(--cream-text);
  }
  .contact__name {
    margin: 0 0 14px;
    font-style: italic;
    font-weight: 400;
    font-size: 45px;
    line-height: 58px;
  }
  .contact__details {
    margin: 0;
    font-style: normal;
    font-size: 36px;
    line-height: 48px;
  }
  .slogan-band {
    position: absolute;
    left: 0;
    right: 0;
    top: 663px;
    height: 46px;
    background: var(--cream);
  }
  .slogan-band__text {
    position: absolute;
    right: 79px;
    top: 0;
    margin: 0;
    color: var(--maroon);
    font-style: italic;
    font-size: 34px;
    line-height: 46px;
  }
</style>
</head>
<body>
  <main class="card">
    <div class="card__backdrop" role="img" aria-label="Maroon background with a subtle interlocking lattice pattern"></div>

    <div class="logo-panel">
      <p class="logo-panel__name">Helena Brackett &amp; Associates<br>Lawyers</p>
    </div>

    <h1 class="firm-title">
      <span class="firm-title__line firm-title__line--first">Helena Brackett &amp; Associates</span>
      <span class="firm-title__line">Lawyers &amp; Conveyancers</span>
    </h1>

    <section class="contact">
      <h2 class="contact__name">Helena Brackett</h2>
      <address class="contact__details">
        LL.B. Principal Solicitor<br>
        17 Quillon Street<br>
        Marrowdale NSW 2190
      </address>
    </section>

    <footer class="slogan-band">
      <p class="slogan-band__text">From our family to yours</p>
    </footer>
  </main>
</body>
</html>
```